Business Card Design For Marketing Agnecy LWP

Need business card design for marketing agency.

Dorian Pellow
President, CEO
1-555-302-4196
dorian@brightlanepromotions.example
www.BrightlanePromotions.example

Back Side:
Boost Sales Using Rewards, Incentives & Giveaways
Get A Free Sample Package

Target Market(s)

B2B

Industry/Entity Type

Marketing

Contact Information for Business Card

Dorian Pellow
President, CEO
1-555-302-4196

Back Side:
Get A Free Sample Package

Please note that my current url is OLD DESIGN. I am working on new design and want the business card to match color themes at least on new site. Here is the demo link for new site so you can see the colors I use, etc.

http://pixelquarrydemo.example/dh/dorian/lwp_final/index.html

Requirements
Must have
• Please note that my current url is OLD DESIGN. I am working on new design and want the business card to match color themes at least on new site. Here is the demo link for new site so you can see the colors I use, etc.

Nice to have

Should not have

```html
<!DOCTYPE html>
<html lang="en">
<head>
<meta charset="utf-8">
<title>LWP Business Card – Front and Back</title>
<link rel="stylesheet" href="https://fonts.googleapis.com/css2?family=Roboto:wght@400;500&family=Roboto+Condensed:wght@400;700&family=Exo+2:wght@800&display=swap">
<style>
  :root {
    --backdrop: #bdbdbd;
    --brand-blue: #2b5997;
    --brand-blue-dark: #24508b;
    --ink-dark: #3a3a3a;
    --ink-grey: #333333;
    --card-light: #f2f2f2;
    --card-light-edge: #dcdcdc;
    --white: #ffffff;
  }
  * { box-sizing: border-box; margin: 0; padding: 0; }
  html, body {
    width: 1200px; height: 576px; overflow: hidden;
    background: var(--backdrop);
  }
  .canvas { position: relative; width: 1200px; height: 576px; }

  .card {
    position: absolute;
    border-radius: 10px;
    overflow: hidden;
  }

  /* Back side */
  .card-back {
    left: 82px; top: 139px; width: 484px; height: 293px;
    background: linear-gradient(180deg, #2d5c9c 0%, var(--brand-blue-dark) 100%);
    color: var(--white);
    text-align: center;
  }
  .card-back .brand-name {
    position: absolute; left: 0; right: 0; top: 58px;
    font-family: "Roboto", sans-serif; font-weight: 500;
    font-size: 64px; line-height: 1; letter-spacing: 2px;
    color: var(--white);
  }
  .offer-banner {
    position: absolute; left: 62px; top: 193px; width: 360px; height: 54px;
  }
  .offer-banner svg { position: absolute; inset: 0; }
  .offer-banner .offer-text {
    position: relative; padding-top: 8px;
  }
  .offer-banner .tagline {
    font-family: "Roboto", sans-serif; font-size: 13.5px; color: var(--ink-grey);
  }
  .offer-banner .cta {
    font-family: "Roboto Condensed", sans-serif; font-weight: 700;
    font-size: 14px; color: var(--brand-blue); margin-top: 3px;
  }
  .card-back .website {
    position: absolute; left: 0; right: 0; top: 256px;
    font-family: "Roboto", sans-serif; font-size: 13px; color: #e6ecf5;
  }

  /* Front side */
  .card-front {
    left: 602px; top: 138px; width: 480px; height: 291px;
    background: linear-gradient(180deg, var(--card-light) 0%, #e8e8e8 60%, var(--card-light-edge) 100%);
  }
  .card-front .brand-name {
    position: absolute; left: 26px; top: 44px;
    font-family: "Roboto", sans-serif; font-weight: 500;
    font-size: 48px; line-height: 1; letter-spacing: 2px;
    color: var(--brand-blue);
  }
  .person { position: absolute; left: 26px; top: 178px; }
  .person .name {
    font-family: "Roboto", sans-serif; font-weight: 500;
    font-size: 19px; color: var(--brand-blue);
  }
  .person .role {
    font-family: "Roboto Condensed", sans-serif; font-size: 13px;
    color: var(--ink-grey); margin-top: 2px;
  }
  .contact-list {
    position: absolute; left: 224px; top: 180px; list-style: none;
    font-family: "Roboto Condensed", sans-serif; font-size: 13px; color: var(--ink-grey);
  }
  .contact-list li { display: flex; align-items: center; gap: 9px; height: 18px; }
  .contact-list svg { width: 11px; height: 11px; fill: var(--ink-dark); flex: none; }

  .footer-band { position: absolute; left: 0; bottom: 0; width: 480px; height: 36px; }
  .footer-band svg { position: absolute; inset: 0; }
  .footer-band .cta {
    position: absolute; right: 30px; bottom: 9px;
    font-family: "Exo 2", sans-serif; font-weight: 800;
    font-size: 13px; letter-spacing: 0.3px; color: var(--white);
    text-transform: uppercase;
  }
</style>
</head>
<body>
<main class="canvas">

  <section class="card card-back" aria-label="Card back side">
    <p class="brand-name">LWP</p>
    <div class="offer-banner">
      <svg viewBox="0 0 360 54" width="360" height="54" aria-hidden="true">
        <path d="M0 0 H360 L352 42 L180 54 L8 42 Z" fill="#f1f1f1"/>
      </svg>
      <div class="offer-text">
        <p class="tagline">Boost Sales Using Rewards, Incentives &amp; Giveaways</p>
        <p class="cta">GET A FREE SAMPLE PACKAGE</p>
      </div>
    </div>
    <p class="website">www.BrightlanePromotions.example</p>
  </section>

  <section class="card card-front" aria-label="Card front side">
    <p class="brand-name">LWP</p>

    <div class="person">
      <p class="name">Dorian Pellow</p>
      <p class="role">President, CEO</p>
    </div>

    <ul class="contact-list">
      <li>
        <svg viewBox="0 0 12 12" aria-hidden="true"><path d="M1 4 Q6 0 11 4 L10 5.5 L8 4.5 V3.8 Q6 3 4 3.8 V4.5 L2 5.5 Z M3 6 H9 L10 11 H2 Z"/></svg>
        1-555-302-4196
      </li>
      <li>
        <svg viewBox="0 0 12 12" aria-hidden="true"><path d="M1 2.5 H11 V9.5 H1 Z M1.8 3.2 L6 6.6 L10.2 3.2" stroke="#f0f0f0" stroke-width="0.9"/></svg>
        dorian@brightlanepromotions.example
      </li>
      <li>
        <svg viewBox="0 0 12 12" aria-hidden="true"><circle cx="6" cy="6" r="5"/><path d="M1 6 H11 M6 1 V11 M6 1 Q3 6 6 11 M6 1 Q9 6 6 11" stroke="#f0f0f0" stroke-width="0.7" fill="none"/></svg>
        www.BrightlanePromotions.example
      </li>
    </ul>

    <div class="footer-band">
      <svg viewBox="0 0 480 36" width="480" height="36" aria-hidden="true">
        <rect x="0" y="25" width="230" height="11" fill="var(--ink-dark)"/>
        <path d="M234 0 H480 V36 H218 Z" fill="var(--brand-blue)"/>
      </svg>
      <span class="cta">Get a free sample package</span>
    </div>
  </section>

</main>
</body>
</html>
```